Real Estate Agent - Sold Brochure

I am a Real Estate Agent who is looking for a SOLD brochure design that looks simple, sharp, classy and elegant. Over the years, I have created a business image for myself that has helped me sell a lot of top end properties with great results. "Jolly Margo, Jolly Vendor" is my logo and the message that I consistently portray to my clients in my area.
I am after a double-sided brochure. On the front I would like a photo of the SOLD property with a watermark "not just sold....sold for a premium". It will also have my company logo, with personal profile photo and personal logo - "Jolly Margo, Jolly Vendor".
On the back, I would like the client testimonial letter and the client sold photo - as well as my personal logo once again - "Jolly Margo, Jolly Vendor".
If you could exercise your artistic imagination as a designer and create something classy and extraordinary.
Please see attached samples of work created previously and feel free to come up with new ideas or improvements.

Additional details: Flyer size to be approx. landscape layout 240mm wide x 130mm high.

Many thanks,
Margo

Additional details: Flyer size to be approx. landscape layout 240mm wide x 130mm high. with rounded corners

```html
<!DOCTYPE html>
<html lang="en">
<head>
<meta charset="utf-8">
<title>Sold Testimonial – Jolly Margo, Jolly Vendor</title>
<link rel="stylesheet" href="https://fonts.googleapis.com/css2?family=Open+Sans:wght@300;400;600&display=swap">
<style>
  :root {
    --brand-red: #c8302e;
    --brand-red-deep: #b3231f;
    --paper: #ffffff;
    --ink: #1f1f1f;
    --logo-ink: #5a1410;
    --logo-dot: #d98a1c;
  }
  * { box-sizing: border-box; margin: 0; padding: 0; }
  html, body {
    width: 1200px; height: 650px; overflow: hidden;
    background: var(--paper);
    font-family: "Open Sans", Arial, sans-serif;
  }
  .flyer {
    position: relative; width: 1200px; height: 650px;
    border-radius: 26px; overflow: hidden;
    background: linear-gradient(180deg, var(--brand-red) 0%, var(--brand-red-deep) 100%);
  }
  .letter {
    position: absolute; left: 32px; top: 76px;
    color: var(--paper); font-weight: 300; font-size: 20.5px; line-height: 25.5px;
    white-space: nowrap;
  }
  .letter p + p { margin-top: 25.5px; }
  .client-photo {
    position: absolute; left: 646px; top: 45px; width: 580px; height: 460px;
    transform: rotate(-9.2deg); transform-origin: center;
    border: 4px solid var(--paper);
    box-shadow: 0 4px 14px rgba(0,0,0,.35);
    background: linear-gradient(180deg, #4d7ec9 0%, #a9c3e3 30%, #8a6a4a 45%, #b88a5c 60%, #4f6b35 85%, #6a7a3e 100%);
  }
  .agent-portrait {
    position: absolute; left: 1058px; top: 318px; width: 142px; height: 254px;
    border-radius: 70px 0 0 0;
    background: linear-gradient(180deg, #5a3a28 0%, #e7c9ae 35%, #f4f4f4 60%, #ffffff 100%);
  }
  .footer-band {
    position: absolute; left: 0; bottom: 0; width: 100%; height: 80px;
    background: var(--paper);
    display: flex; align-items: center; justify-content: space-between;
    padding: 0 20px 0 38px;
  }
  .company-mark { display: flex; align-items: center; gap: 12px; }
  .company-name {
    font-size: 22px; font-weight: 400; color: var(--logo-ink); letter-spacing: .5px;
  }
  .tagline {
    font-size: 43px; font-weight: 300; color: var(--ink); letter-spacing: 7.5px;
  }
</style>
</head>
<body>
  <main class="flyer">
    <article class="letter">
      <p>Testimonial Letter</p>
      <p>42 Wattlebird Close, Marrowdale<br>
      After having the house on sale with various other agents and<br>
      receiving only lukewarm service and low offers we were very<br>
      impressed with your sale strategy which resulted in the best<br>
      open house we ever had and multiple good offers, some<br>
      higher than the asking price leading to us accepting a good<br>
      offer and being able to move on.<br>
      We have already recommended your services to a neighbour<br>
      who is thinking of selling and would be comfortable in<br>
      recommending your services to anyone in the area thinking<br>
      of selling. It was a real pleasure to have had you represent our<br>
      interested in the sale of our house.</p>
      <p>Rosalind Ferreira</p>
    </article>

    <div class="client-photo" role="img" aria-label="Photo of the agent with the happy sellers in front of their brick house beside a sold sign"></div>
    <div class="agent-portrait" role="img" aria-label="Portrait of agent Margo"></div>

    <footer class="footer-band">
      <div class="company-mark">
        <span class="company-name">Harlow &amp; Finch</span>
        <svg width="30" height="30" aria-hidden="true"><circle cx="15" cy="15" r="14" fill="var(--logo-dot)"/></svg>
      </div>
      <div class="tagline">Jolly Margo, Jolly Vendor</div>
    </footer>
  </main>
</body>
</html>
```